Graphic Design Project - Coffee Label

I am a coffee roasting business and I need a professional label design for my bag of coffee. this needs to be in a format that we can change the "title" or "weight" of the product frequently ourselves. We do have photoshop, but cannot create the project, but can edit if need be to print. Our labels are 3"x8". we will want the colors to bleed to the end. The labels are white and glossy, but i want the design to give the illusion that the color of the label is not evident. I have a logo. I do not want the design to have a border. Since the label is only 3" wide and 8" tall the design needs to be creative to look good. although coffee colors are ok, I want a lot more color to not be boring. We could frequently change the label size and would need to adjust accordingly from the current design.
Updates

Project Deadline Extended
Reason: I just decided to remove my refundable contract into committed payment to a designer. I would like a few more days to broadcast that option.

Target Market(s)

30-50 year olds that have money and want to buy quality

Industry/Entity Type

Business

Requirements
Must have
• we currently are using label 3" wide and 8" tall. First and foremost I need to be able to edit the words on the label. I will need to change the net wt and the coffee blend names. I would like the ability to change the size if need be. the company name is
1. Heron Dusk Coffee
2. Artisan Coffee Roasting
3. Needs to be a large space for a particular coffee name i.e Rain, Fern and Pebble Blend. Use this blend, but I need to be able to edit it for other blends.
4. Under the blend it should say Whole Bean. Also need to be able to edit.
5. At the bottom it should say Roasted in Brookfield, Oregon. www.herondusk-example.com
6. Below the coffee name there should be Net Weight ie 16 oz (this also needs to be editable for us)
Nice to have
• I have a logo, but it can be different. Labels are white, but I don't want borders, and would like the colors to bleed and not to appear to be a white label. the bags are light grey/silver metallic. Although many use a lot of "coffee" colors for design, I do not. I have pics of coffee beans; it doesn't have to be used. I don't want to be just a block of a pic of beans. Other pics of coffee related ideas is fine with me. I don't need the brand to dominate the label. Bolder colors. I have attached roasting pics. These do not have to be used, but can. If used please edit out the extraneous background.
Should not have
• Do not use borders. I want the colors to bleed to the end. I don't want the white label to show through as though I have a typed page of print. I don't want just coffee colors used. I don't want light colors. I don't want a "square" looking format wherein everything is just line by line. Asymmetrical is ok.

```html
<!DOCTYPE html>
<html lang="en">
<head>
<meta charset="utf-8">
<title>Heron Dusk Coffee – Label</title>
<link rel="stylesheet" href="https://fonts.googleapis.com/css2?family=Bellefair&family=Arimo:wght@700&family=Fredoka:wght@600&display=swap">
<style>
  :root {
    --backdrop-light: #e4e4e2;
    --backdrop-dark: #b5b3b0;
    --label-top: #b8342a;
    --label-mid: #c38a2e;
    --label-low: #c0562a;
    --seal-red-top: #ad1f24;
    --seal-red-low: #84151a;
    --logo-orange: #e2682c;
    --logo-gold: #eb962f;
    --title-yellow: #ffe500;
    --text-white: #ffffff;
  }
  * { margin: 0; padding: 0; box-sizing: border-box; }
  html, body { width: 1200px; height: 1000px; overflow: hidden; }
  body {
    background: radial-gradient(ellipse at center, var(--backdrop-light) 35%, var(--backdrop-dark) 100%);
    position: relative;
    font-family: "Arimo", sans-serif;
  }
  .label {
    position: absolute;
    left: 444px; top: 40px;
    width: 346px; height: 924px;
    overflow: hidden;
    box-shadow: 0 0 18px rgba(0,0,0,0.25);
  }
  .label-art { position: absolute; inset: 0; }
  .brand-title text {
    font-family: "Bellefair", serif;
    fill: var(--title-yellow);
  }
  .text {
    position: absolute; left: 0; width: 100%;
    text-align: center; color: var(--text-white);
    font-weight: 700;
  }
  .logo-name {
    position: absolute; left: 92px; top: 88px; width: 162px;
    text-align: center; color: var(--logo-gold);
    font-family: "Arimo", sans-serif; font-weight: 700;
    font-size: 20px; line-height: 24px;
  }
  .tagline { top: 602px; font-size: 24px; line-height: 28px; letter-spacing: -0.3px; }
  .blend-name {
    top: 708px;
    font-family: "Fredoka", sans-serif; font-weight: 600;
    font-size: 32px; line-height: 30px; letter-spacing: -1.6px;
  }
  .bean-type { top: 780px; font-size: 22px; line-height: 26px; }
  .net-weight { top: 843px; font-size: 16px; line-height: 20px; }
  .roast-origin { top: 877px; font-size: 16px; line-height: 19px; }
</style>
</head>
<body>
  <div class="label">
    <svg class="label-art" width="346" height="924" viewBox="0 0 346 924" aria-hidden="true">
      <defs>
        <linearGradient id="labelGround" x1="0" y1="0" x2="0" y2="1">
          <stop offset="0" stop-color="var(--label-top)"/>
          <stop offset="0.22" stop-color="#bd5a2b"/>
          <stop offset="0.7" stop-color="var(--label-mid)"/>
          <stop offset="1" stop-color="var(--label-low)"/>
        </linearGradient>
        <linearGradient id="sealRed" x1="0" y1="0" x2="0" y2="1">
          <stop offset="0" stop-color="var(--seal-red-top)"/>
          <stop offset="1" stop-color="var(--seal-red-low)"/>
        </linearGradient>
      </defs>
      <rect width="346" height="924" fill="url(#labelGround)"/>
      <circle class="logo-ring" cx="172" cy="100" r="80" fill="none" stroke="var(--logo-orange)" stroke-width="11"/>
      <circle class="title-seal" cx="173" cy="438" r="260" fill="url(#sealRed)"/>
      <ellipse class="footer-band" cx="173" cy="1000" rx="330" ry="182" fill="var(--seal-red-top)"/>
    </svg>

    <div class="logo-name">Heron Dusk</div>

    <svg class="label-art brand-title" width="346" height="924" viewBox="0 0 346 924" role="heading" aria-level="1" aria-label="Heron Dusk Coffee">
      <text x="19" y="344" font-size="165" textLength="307" lengthAdjust="spacingAndGlyphs">HERON</text>
      <text x="23" y="488" font-size="200" textLength="309" lengthAdjust="spacingAndGlyphs">DUSK</text>
      <text x="26" y="600" font-size="165" textLength="282" lengthAdjust="spacingAndGlyphs">COFFEE</text>
    </svg>

    <p class="text tagline">Artisan Coffee Roasting</p>

    <h2 class="text blend-name">Rain, Fern &amp; Pebble<br>Blend.</h2>
    <p class="text bean-type">Whole Bean</p>

    <p class="text net-weight">Net Weight 16 oz</p>
    <p class="text roast-origin">Roasted in Brookfield, Oregon.<br>www.herondusk-example.com</p>
  </div>
</body>
</html>
```